Webdesign für Metallverarbeitung
Zielgruppe
Metallverarbeitung, Verpackung, Automobilzulieferer, Lasertechnik, Elektrotechnik, CAD Verarbeitung
Aufgabenstellung
-Farbe: Blau/Silber Edelstahllook,
-Logo anbei
- Modernes Team, Flexibilität, Dynamik
- Metallverarbeitendes Unternehmen
- Automobil
-Elektroindustrie

```html
<!DOCTYPE html>
<html lang="de">
<head>
<meta charset="utf-8">
<title>Norvatek Metallbau – Start</title>
<link rel="stylesheet" href="https://fonts.googleapis.com/css2?family=Open+Sans:wght@300;400;600;700;800&display=swap">
<style>
:root{
  --navy:#0c3a60;
  --cyan:#18a7d8;
  --silver-1:#e9e9ea;
  --silver-2:#c4c5c7;
  --silver-3:#f6f6f6;
  --band:#f4f4f4;
  --white:#ffffff;
  --photo-dark:#1d2f4e;
  --photo-mid:#3d5f86;
  --overlay:#2f5478;
}
*{margin:0;padding:0;box-sizing:border-box}
html,body{width:1200px;height:2177px;overflow:hidden;background:var(--white)}
body{position:relative;font-family:"Open Sans",sans-serif;color:var(--navy)}
.bg{position:absolute;left:0;top:0;width:1200px;height:2177px}
.abs{position:absolute}
.brand{display:flex;align-items:center;gap:10px;font-weight:800;font-size:22px;color:var(--navy);letter-spacing:.5px}
.brand-dot{width:30px;height:30px;border-radius:50%;background:var(--navy)}
.nav{position:absolute;top:69px;left:0;width:1200px;height:20px}
.nav a{position:absolute;top:0;font-size:13.5px;font-weight:600;letter-spacing:1.4px;color:var(--navy);text-decoration:none}
.nav a.active{color:var(--cyan)}
.hero-title{left:84px;top:296px;font-size:58px;font-weight:300;letter-spacing:-.5px;white-space:nowrap}
.hero-sub{left:83px;top:362px;font-size:23px;font-weight:600;letter-spacing:.6px;white-space:nowrap}
.hero-photo{left:607px;top:210px;width:450px;height:350px;background:linear-gradient(180deg,#cfd6de 0%,#8e9cb0 30%,#2a4f83 55%,#1a2946 80%,#13203a 100%);box-shadow:0 10px 24px rgba(0,0,0,.28)}
.intro{left:200px;width:800px;top:636px;text-align:center}
.intro h1{font-size:27px;font-weight:800;line-height:35px}
.intro p{margin-top:11px;font-size:13.6px;line-height:22.5px;padding:0 60px}
.btn{position:absolute;left:505px;top:815px;width:169px;height:33px;border-radius:17px;background:var(--cyan);color:var(--white);font-size:15px;font-weight:800;letter-spacing:2px;display:flex;align-items:center;justify-content:center}
.choose{left:0;width:1200px;top:1015px;text-align:center;font-size:27px;font-weight:800}
.tile{position:absolute;display:flex;align-items:center;justify-content:center;color:var(--white);font-weight:800;box-shadow:0 8px 16px rgba(0,0,0,.12)}
.tile.lg{font-size:42px;top:1075px;width:358px;height:176px}
.tile.sm{font-size:38px;top:1550px;width:311px;height:223px;box-shadow:none}
.foot-contact{font-size:14px;line-height:22.5px;color:var(--navy)}
.foot-bottom{top:2138px;font-size:13px;font-weight:600;letter-spacing:.8px}
.foot-bottom.link{text-decoration:underline}
</style>
</head>
<body>
<svg class="bg" viewBox="0 0 1200 2177" aria-hidden="true">
  <defs>
    <linearGradient id="steel" x1="0" y1="0" x2="1" y2="1">
      <stop offset="0" stop-color="#d8d9db"/>
      <stop offset=".35" stop-color="#f3f3f4"/>
      <stop offset=".6" stop-color="#c9cacc"/>
      <stop offset=".85" stop-color="#eeeeef"/>
      <stop offset="1" stop-color="#d1d2d4"/>
    </linearGradient>
  </defs>
  <polygon points="0,0 1200,0 1200,406 0,529" fill="url(#steel)"/>
  <polygon points="0,870 1200,997 1200,1430 0,1306" fill="#f4f4f4"/>
  <polygon points="0,2018 1200,1891 1200,2177 0,2177" fill="url(#steel)"/>
</svg>

<div class="abs brand" style="left:47px;top:50px"><span class="brand-dot"></span>Norvatek</div>

<nav class="nav">
  <a class="active" style="left:329px">START</a>
  <a style="left:429px">ÜBER UNS</a>
  <a style="left:558px">LEISTUNGEN</a>
  <a style="left:707px">TEAM</a>
  <a style="left:803px">REFERENZEN</a>
  <a style="left:954px">GALLERIE</a>
  <a style="left:1078px">KONTAKT</a>
</nav>

<div class="abs hero-title">Made in Germany</div>
<div class="abs hero-sub">Wir halten unser Qualitätsversprechen!</div>
<div class="abs hero-photo" role="img" aria-label="Foto: Laserschneidkopf schneidet Blech mit Funken"></div>

<section class="abs intro">
  <h1>Schnelle und präzise Auftragsbearbeitung<br>bei höchster Flexibilität.</h1>
  <p>Wir sind Ihr zuverlässigster Partner von der Konstruktion / Entwicklung bis zum fertig veredelten Endprodukt. Dabei denken wir innovativ, arbeiten kreativ und kombinieren die traditionelle Handwerkskunst mit aktuellem Design.</p>
</section>
<div class="btn">ÜBER UNS</div>

<div class="abs choose">Wählen Sie bitte zwischen:</div>
<div class="tile lg" style="left:236px;background:linear-gradient(135deg,#4d6f92,#2b4e74 60%,#3e6388)" role="img" aria-label="Foto: Hände montieren Industriemaschine">Industry</div>
<div class="tile lg" style="left:607px;background:linear-gradient(180deg,#2f5d93 0%,#34506e 30%,#3a4f66 100%)" role="img" aria-label="Foto: Metallzaun mit waagerechten Lamellen">Home</div>

<div class="tile sm" style="left:112px;background:linear-gradient(135deg,#4c6f91,#2f5478 55%,#6b7d7e)" role="img" aria-label="Foto: Mitarbeiter mit Schutzhelm in der Werkhalle">Team</div>
<div class="tile sm" style="left:444px;background:linear-gradient(135deg,#6e8aa6,#3f5f80 55%,#4f6e8c)" role="img" aria-label="Foto: Gitterrost aus Metall">Referenzen</div>
<div class="tile sm" style="left:786px;background:linear-gradient(135deg,#2f5478,#7794b1 55%,#3c5f82)" role="img" aria-label="Foto: lasergeschnittene Metallfigur">Gallerie</div>

<div class="abs brand" style="left:870px;top:2002px;font-size:28px"><span class="brand-dot" style="width:38px;height:38px"></span>Norvatek</div>
<div class="abs foot-contact" style="left:868px;top:2088px">Lindenweg 24<br>12345 Musterstadt<br>info@norvatek-metall.de</div>
<div class="abs foot-contact" style="left:1034px;top:2088px">+49 123 4567810<br>+49 170 1234567<br>+49 123 4567811</div>

<div class="abs foot-bottom" style="left:52px">© 2022 Norvatek Metallbau GmbH</div>
<div class="abs foot-bottom link" style="left:423px">Impressum</div>
<div class="abs foot-bottom link" style="left:553px">Datenschutz</div>
<div class="abs foot-bottom link" style="left:696px">Kontakt</div>
</body>
</html>
```